Powepoint template for an investment group

Need high end clear clean concise creative luxurious

Have royal clients
High end/billionaire investors

Using ross gold logo can be creative
Must habe page numbers
Logo preference header top right
Page number footer bottom right

The first page of the ppt maybe a big block of dark grey and oberi investment group written on the front page in rose gold

Target Market(s)

Investors at a high level

Requirements
Must have
• Luxury feel

```html
<!DOCTYPE html>
<html lang="en">
<head>
<meta charset="utf-8">
<title>Oberi Investment Group – Presentation Template</title>
<link href="https://fonts.googleapis.com/css2?family=Josefin+Sans:wght@200;300&family=Poppins:wght@300;400;600&family=Open+Sans:wght@400&family=Cormorant+Garamond:wght@500&display=swap" rel="stylesheet">
<style>
  :root{
    --board:#e1e1e1;
    --ink:#050608;
    --white:#ffffff;
    --rose:#d9a49b;
    --rose-deep:#c98377;
    --rose-dark:#9c5a52;
    --taupe:#a3928d;
    --bar-pink:#efbeb4;
    --label:#3d4a6b;
    --text:#1a1a1a;
  }
  *{margin:0;padding:0;box-sizing:border-box}
  html,body{width:1200px;height:1155px;overflow:hidden;background:var(--board)}
  .board{position:relative;width:1200px;height:1155px}
  .slide-frame{position:absolute;width:514px;height:289px;overflow:hidden}
  .slide{position:absolute;left:0;top:0;width:840px;height:472px;transform:scale(0.612);transform-origin:0 0;overflow:hidden}
  .slide svg.shapes{position:absolute;left:0;top:0}
  .dark{background:var(--ink)}
  .light{background:var(--white)}

  .brand{position:absolute;font-family:"Josefin Sans",sans-serif;font-weight:200;color:var(--rose);text-align:center;line-height:1;white-space:nowrap}
  .brand .name{display:block;font-size:76px;letter-spacing:22px;margin-right:-22px}
  .brand .sub{display:block;font-size:25px;letter-spacing:2px;margin-top:14px}
  .brand--cover .name{font-size:64px;letter-spacing:15px;margin-right:-15px}
  .brand--cover .sub{font-size:24px;margin-top:12px}
  .web{position:absolute;display:flex;align-items:center;gap:12px;font-family:"Cormorant Garamond",serif;font-weight:500;font-size:14px;color:#d8d0cc}

  .cover-title{position:absolute;left:47px;top:348px;font-family:"Poppins",sans-serif;font-weight:600;font-size:40px;line-height:46px;color:var(--white)}

  .contents-title{position:absolute;left:73px;top:96px;font-family:"Open Sans",sans-serif;font-size:29px;color:var(--text)}
  .toc{position:absolute;left:73px;top:145px;width:347px;border-collapse:collapse;font-family:"Open Sans",sans-serif;font-size:15px;color:var(--text)}
  .toc td{height:44.5px;vertical-align:middle;padding-top:2px}
  .toc tr:not(:last-child) td{border-bottom:2px solid var(--text)}
  .toc td.page{width:87px;padding-left:26px;border-left:2px solid var(--text)}
  .toc tr:last-child td{height:48px}

  .mission{position:absolute;right:35px;top:292px;width:276px;font-family:"Poppins",sans-serif;color:var(--text)}
  .mission h2{font-weight:400;font-size:26px;text-align:right;margin-bottom:4px}
  .mission p{font-weight:300;font-size:15px;line-height:21px;text-align:justify;text-align-last:justify}

  .overview{position:absolute;left:532px;top:58px;width:266px;font-family:"Poppins",sans-serif;font-weight:300;font-size:14.6px;line-height:21px;text-align:justify;color:var(--text)}
  .chart{position:absolute;left:532px;top:276px}
  .chart .label{position:absolute;top:0;width:35px;text-align:center;font-family:"Poppins",sans-serif;font-weight:600;font-size:13px;color:var(--label);border-bottom:2px solid var(--label);line-height:18px}

  .services{position:absolute;left:50px;top:30px;width:740px;font-family:"Open Sans",sans-serif;color:var(--text)}
  .services h2{font-weight:400;font-size:31px;line-height:40px}
  .services .tag{font-size:18px;border-left:2px solid var(--rose);padding-left:6px;margin:4px 0 18px 3px;line-height:22px}
  .services p{font-size:13.2px;line-height:17.4px;text-align:justify}
  .services p.first{padding:0 1px 0 3px}
  .services hr{border:0;border-top:2px solid var(--rose);margin:12px 0 36px}
</style>
</head>
<body>
<main class="board">

  <!-- Cover -->
  <section class="slide-frame" style="left:66px;top:95px">
    <div class="slide dark">
      <svg class="shapes" width="840" height="472" viewBox="0 0 840 472">
        <defs>
          <linearGradient id="towerTone" x1="0" y1="0" x2="1" y2="1">
            <stop offset="0" stop-color="#4a3a30"/>
            <stop offset="0.55" stop-color="#2a211c"/>
            <stop offset="1" stop-color="#0e0b0a"/>
          </linearGradient>
        </defs>
        <polygon role="img" aria-label="Photo looking up a tall building facade" fill="url(#towerTone)" points="0,0 340,0 480,236 340,472 0,472"/>
        <polygon fill="var(--rose)" points="340,0 378,0 518,236 378,472 340,472 480,236"/>
        <polygon fill="var(--rose-deep)" points="450,130 500,130 565,236 500,343 450,343 515,236"/>
        <polygon fill="var(--rose)" points="402,0 420,0 435,22 417,22"/>
        <polygon fill="var(--rose)" points="417,450 435,450 420,472 402,472"/>
      </svg>
      <h1 class="cover-title">INVESTMENT<br>GROUP</h1>
      <div class="brand brand--cover" style="left:530px;top:48px;width:280px">
        <span class="name">OBERI</span><span class="sub">Investment Group</span>
      </div>
      <div class="web" style="left:637px;top:420px">
        <svg width="18" height="18" viewBox="0 0 18 18"><circle cx="9" cy="9" r="8" fill="none" stroke="var(--rose)" stroke-width="1.4"/><path d="M7 5l5 4-2.3.4L11 12l-1 .5-1.3-2.6L7 11.5z" fill="var(--rose)"/></svg>
        www.oberi-invest.com
      </div>
    </div>
  </section>

  <!-- Contents -->
  <section class="slide-frame" style="left:620px;top:95px">
    <div class="slide light">
      <div class="contents-title">CONTENTS</div>
      <table class="toc">
        <tr><td>COMPANY OVERVIEW</td><td class="page">02</td></tr>
        <tr><td>OUR SERVICES</td><td class="page">04</td></tr>
        <tr><td>PROFFESIONAL SERVICES</td><td class="page">20</td></tr>
        <tr><td>WHAT WE DO</td><td class="page">20</td></tr>
        <tr><td>OUR CLIENTS</td><td class="page">30</td></tr>
      </table>
      <svg class="shapes" width="840" height="472" viewBox="0 0 840 472" style="pointer-events:none">
        <defs>
          <linearGradient id="deskTone" x1="0" y1="0" x2="1" y2="1">
            <stop offset="0" stop-color="#cfa79c"/>
            <stop offset="1" stop-color="#b98f86"/>
          </linearGradient>
        </defs>
        <rect role="img" aria-label="Rose tinted photo of hands writing beside a laptop" x="473" y="0" width="367" height="472" fill="url(#deskTone)"/>
      </svg>
    </div>
  </section>

  <!-- Mission -->
  <section class="slide-frame" style="left:66px;top:431px">
    <div class="slide light">
      <svg class="shapes" width="840" height="472" viewBox="0 0 840 472">
        <defs>
          <linearGradient id="tradeTone" x1="0" y1="0" x2="1" y2="1">
            <stop offset="0" stop-color="#414858"/>
            <stop offset="1" stop-color="#262b36"/>
          </linearGradient>
        </defs>
        <polygon role="img" aria-label="Dark photo of a businessman reviewing financial figures" fill="url(#tradeTone)" points="0,0 840,0 840,115 120,472 0,472"/>
        <polygon fill="var(--taupe)" points="310,398 625,245 625,265 310,420"/>
        <polygon fill="var(--rose-dark)" points="327,372 625,237 625,262 327,398"/>
        <polygon fill="var(--rose)" points="327,365 770,142 770,178 327,400"/>
      </svg>
      <div class="mission">
        <h2>Our Mission</h2>
        <p>Oberi Investment Group has been investing its own capital since 1998 and has had a prestigious track record generating over $2 Billion in enterprise value across various industries</p>
      </div>
    </div>
  </section>

  <!-- Overview with chart -->
  <section class="slide-frame" style="left:620px;top:431px">
    <div class="slide light">
      <svg class="shapes" width="840" height="472" viewBox="0 0 840 472">
        <defs>
          <linearGradient id="signTone" x1="0" y1="0" x2="1" y2="1">
            <stop offset="0" stop-color="#4a5060"/>
            <stop offset="0.6" stop-color="#6a6f6c"/>
            <stop offset="1" stop-color="#3c4250"/>
          </linearGradient>
        </defs>
        <polygon fill="var(--taupe)" points="14,28 40,28 92,260 80,268"/>
        <polygon fill="var(--rose)" points="20,0 130,0 70,262"/>
        <polygon role="img" aria-label="Photo of a hand signing a document with a pen" fill="url(#signTone)" points="130,0 500,0 440,240 500,472 20,472 70,262"/>
        <polygon fill="var(--taupe)" points="440,240 506,445 490,445"/>
        <polygon fill="var(--rose-dark)" points="440,240 492,445 478,445"/>
        <polygon fill="var(--rose)" points="440,240 500,472 390,472"/>
      </svg>
      <p class="overview">Oberi Investment Group has been investing its own capital since 1998 and has had a prestigious track record generating over $2 Billion in enterprise value across various industries including financial services, software, biotechnology, advanced manufacturing, and alternative energy.</p>
      <div class="chart">
        <span class="label" style="left:2px">60%</span>
        <span class="label" style="left:55px">80%</span>
        <span class="label" style="left:108px">50%</span>
        <span class="label" style="left:161px">40%</span>
        <span class="label" style="left:214px">70%</span>
        <svg width="270" height="170" viewBox="0 0 270 170" style="position:absolute;left:0;top:28px">
          <g fill="var(--bar-pink)">
            <rect x="9" y="0" width="20" height="60"/><rect x="62" y="0" width="20" height="30"/>
            <rect x="115" y="0" width="20" height="75"/><rect x="168" y="0" width="20" height="90"/>
            <rect x="221" y="0" width="20" height="45"/>
          </g>
          <g fill="var(--ink)">
            <rect x="2" y="55" width="35" height="85"/><rect x="55" y="27" width="35" height="113"/>
            <rect x="108" y="70" width="35" height="70"/><rect x="161" y="84" width="35" height="56"/>
            <rect x="214" y="41" width="35" height="99"/>
          </g>
        </svg>
      </div>
    </div>
  </section>

  <!-- Services -->
  <section class="slide-frame" style="left:66px;top:770px">
    <div class="slide light">
      <div class="services">
        <h2>Our Services</h2>
        <div class="tag">Best Solutions</div>
        <p class="first">Lorem ipsum dolor sit amet, consectetuer adipiscing elit, sed diam nonummy nibh euismod tincidunt ut laoreet dolore magna aliquam erat volutpat. Ut wisi enim ad minim veniam, quis nostrud exerci tation ullamcorper suscipit lobortis nisl ut aliquip ex ea commodo consequat. Duis autem vel eum iriure dolor in hendrerit in vulputate velit esse molestie consequat, vel illum dolore eu feugiat nulla facilisis at vero eros et accumsan et iusto odio dignissim qui blandit praesent luptatum zzril delenit augue duis dolore te feugait nulla facilisi.</p>
        <hr>
        <p>Oberi Investment Group has been investing its own capital since 1998 and has had a prestigious track record generating over $2 Billion in enterprise value across various industries including financial services, software, biotechnology, advanced manufacturing, and alternative energy.</p>
        <hr>
        <p>The entrepreneurial heritage and innovative spirit of the firm allows it to take unconventional and creative approaches to investing, that are often contrarian and sometimes pioneering.</p>
      </div>
    </div>
  </section>

  <!-- Closing -->
  <section class="slide-frame" style="left:620px;top:770px">
    <div class="slide dark">
      <svg class="shapes" width="840" height="472" viewBox="0 0 840 472">
        <defs>
          <radialGradient id="closingTone" cx="0.5" cy="0.1" r="0.9">
            <stop offset="0" stop-color="#2c231f"/>
            <stop offset="1" stop-color="#070708"/>
          </radialGradient>
        </defs>
        <rect role="img" aria-label="Dark photo looking up a tall building facade" width="840" height="472" fill="url(#closingTone)"/>
        <polygon fill="var(--rose)" points="198,0 226,0 252,32 98,292 62,292 222,32"/>
        <polygon fill="var(--rose)" points="740,212 778,212 625,472 585,472"/>
      </svg>
      <div class="brand" style="left:250px;top:180px;width:340px">
        <span class="name">OBERI</span><span class="sub">Investment Group</span>
      </div>
      <div class="web" style="left:338px;top:388px">
        <svg width="18" height="18" viewBox="0 0 18 18"><circle cx="9" cy="9" r="8" fill="none" stroke="var(--rose)" stroke-width="1.4"/><path d="M7 5l5 4-2.3.4L11 12l-1 .5-1.3-2.6L7 11.5z" fill="var(--rose)"/></svg>
        www.oberi-invest.com
      </div>
    </div>
  </section>

</main>
</body>
</html>
```